Holiday Rental Company Flyer Design (DL not A5)

Project Brief:
We need a double sided DL flyer designed for an up market Holiday Rental Company that portrays a personalised approach to property management. These are to be used for letter box drops to homes we're specifically targeting so the design should be modern, complimentary colour palette, uncluttered & visually appealing.

Please Download the DL Template from Quillmark here: http://www.quillmark-example.com.au/vp/ns/propath/UploadResources.aspx?selectedTab=0?pfid=BFB&pf_id=BFB&xnav=easypath-upload-image#Templates

Target Market(s)

Wealthy Home Owners

Industry/Entity Type

It Company

Font styles to use
Other font styles liked:
• Avant Garde Extra Light & Demi

Colors
33b8a4

Requirements
Must have
• DL Flyer sizes (210mm width x 99mm width, plus 3mm bleed)
• Front: Logo, Main Image & Grab
• Back: Contact Details & Brief Description of our business
• Images: Ideally the main image should be the house with the pool but alternatively a lifestyle images could also be used.
Nice to have
• A creative designer!
Should not have
• Clutter & busy designs

```html
<!DOCTYPE html>
<html lang="en">
<head>
<meta charset="utf-8">
<title>Harbour Retreats – DL Flyer Back</title>
<link rel="stylesheet" href="https://fonts.googleapis.com/css2?family=Poppins:wght@200;300;500;600&display=swap">
<style>
  :root {
    --stage: #e4e6e3;
    --charcoal: #3e3d40;
    --ice: #eff8f8;
    --teal: #1fa98a;
    --ink: #2b2b2d;
    --grey-text: #6d6d70;
    --white: #ffffff;
    --veil: rgba(255, 255, 255, 0.72);
    --veil-soft: rgba(255, 255, 255, 0.5);
  }
  * { box-sizing: border-box; margin: 0; padding: 0; }
  html, body {
    width: 1200px; height: 900px; overflow: hidden;
    background: var(--stage);
    font-family: "Poppins", "Helvetica Neue", Arial, sans-serif;
  }
  .flyer {
    position: absolute; left: 72px; top: 202px;
    width: 1056px; height: 496px;
    display: flex;
    box-shadow: 0 6px 18px rgba(0,0,0,0.18);
  }
  .panel { position: relative; width: 352px; height: 100%; overflow: hidden; }

  /* Left panel */
  .panel--story { background: #d9d9d7; }
  .story-photo {
    position: absolute; inset: 0;
    background: linear-gradient(160deg, #c9c9c6 0%, #e6e5e1 40%, #bdbdba 70%, #d8d7d3 100%);
  }
  .story-rule { position: absolute; background: var(--white); }
  .story-rule--vertical { left: 17px; top: 0; width: 1px; height: 232px; }
  .story-rule--upper { left: 210px; top: 222px; width: 143px; height: 1px; }
  .story-rule--lower { left: 0; top: 474px; width: 163px; height: 1px; }
  .story-title-box {
    position: absolute; left: 24px; top: 252px; width: 287px; height: 80px;
    background: var(--veil); padding: 6px 0 0 50px;
  }
  .story-title {
    font-weight: 200; font-size: 31px; line-height: 33px; color: #3a3a3c;
  }
  .story-body-box {
    position: absolute; left: 24px; top: 332px; width: 318px; height: 135px;
    background: var(--veil-soft); padding: 12px 0 0 50px;
  }
  .story-body {
    font-weight: 300; font-size: 14px; line-height: 19.5px; color: #7a7a7c; width: 250px;
  }

  /* Middle panel */
  .panel--service { background: var(--charcoal); color: var(--white); }
  .service-lines { position: absolute; left: 0; top: 0; }
  .service-intro {
    position: absolute; left: 0; top: 86px; width: 352px;
    text-align: center; font-weight: 200; font-size: 15px; line-height: 19.5px;
  }
  .service-list { list-style: none; position: absolute; left: 56px; top: 246px; }
  .service-item {
    display: flex; gap: 12px; margin-bottom: 36px;
    font-weight: 500; font-size: 13px; line-height: 20px;
  }
  .service-item svg { flex: none; margin-top: 5px; }

  /* Right panel */
  .panel--contact { background: var(--ice); }
  .contact-lines { position: absolute; left: 0; top: 0; }
  .brand {
    position: absolute; left: 0; top: 90px; width: 352px;
    display: flex; justify-content: center; align-items: center; gap: 10px;
    color: var(--teal); font-weight: 300; font-size: 19px; letter-spacing: 0.5px;
  }
  .brand-dot { width: 12px; height: 12px; border: 1.5px solid var(--teal); border-radius: 50%; }
  .contact-lead {
    position: absolute; left: 72px; top: 170px; width: 240px;
    font-weight: 300; font-size: 14.5px; line-height: 19.5px; color: var(--grey-text);
  }
  .contact-icons { position: absolute; left: 71px; top: 302px; display: flex; gap: 8px; }
  .contact-details { position: absolute; left: 72px; top: 340px; color: var(--ink); }
  .contact-phone { font-weight: 600; font-size: 16px; line-height: 24px; }
  .contact-line { font-weight: 500; font-size: 13px; line-height: 23px; }
  .contact-line--web { color: var(--teal); }
  .contact-bar {
    position: absolute; left: 337px; top: 289px; width: 15px; height: 207px; background: var(--teal);
  }
</style>
</head>
<body>
<main class="flyer">
  <section class="panel panel--story">
    <div class="story-photo" role="img" aria-label="Bathroom with grey tiles and a vase of white flowers"></div>
    <span class="story-rule story-rule--vertical"></span>
    <span class="story-rule story-rule--upper"></span>
    <span class="story-rule story-rule--lower"></span>
    <div class="story-title-box"><h1 class="story-title">What we do<br>differently</h1></div>
    <div class="story-body-box">
      <p class="story-body">Rather than relying upon a key safe or a central pick-up destination, a ‘Harbour Retreats’ staff member will greet guests upon arrival.</p>
    </div>
  </section>

  <section class="panel panel--service">
    <svg class="service-lines" width="120" height="90" viewBox="0 0 120 90" aria-hidden="true">
      <line x1="0" y1="74" x2="74" y2="0" stroke="#fff" stroke-width="2"/>
      <line x1="20" y1="78" x2="92" y2="2" stroke="#fff" stroke-width="4"/>
    </svg>
    <p class="service-intro">Our ‘Meet &amp; Greet’<br>service provides home<br>owners with an<br>increased level of<br>Security and also<br>allows us to:</p>
    <ul class="service-list">
      <li class="service-item">
        <svg width="14" height="14" viewBox="0 0 14 14" aria-hidden="true"><polygon points="7,1.5 12.5,5.5 10.4,12 3.6,12 1.5,5.5" fill="none" stroke="#fff" stroke-width="1.4"/></svg>
        <span>Prepare the home for their arrival<br>(lights, heaters, music etc.)</span>
      </li>
      <li class="service-item">
        <svg width="14" height="14" viewBox="0 0 14 14" aria-hidden="true"><polygon points="7,1.5 12.5,5.5 10.4,12 3.6,12 1.5,5.5" fill="none" stroke="#fff" stroke-width="1.4"/></svg>
        <span>Establish a rapport &amp; help<br>facilitate future bookings</span>
      </li>
      <li class="service-item">
        <svg width="14" height="14" viewBox="0 0 14 14" aria-hidden="true"><polygon points="7,1.5 12.5,5.5 10.4,12 3.6,12 1.5,5.5" fill="none" stroke="#fff" stroke-width="1.4"/></svg>
        <span>Reiterate their responsibilities to<br>ensure the return of their bond</span>
      </li>
    </ul>
  </section>

  <section class="panel panel--contact">
    <svg class="contact-lines" width="150" height="135" viewBox="0 0 150 135" aria-hidden="true">
      <line x1="0" y1="128" x2="128" y2="0" stroke="#1fa98a" stroke-width="2"/>
      <line x1="60" y1="82" x2="144" y2="0" stroke="#1fa98a" stroke-width="4"/>
    </svg>
    <div class="brand"><span class="brand-dot"></span><span>Harbour Retreats</span></div>
    <p class="contact-lead">If you’d like to know what your property could achieve or require additional information, please contact us on:</p>
    <div class="contact-icons" aria-hidden="true">
      <svg width="36" height="36" viewBox="0 0 36 36"><circle cx="18" cy="18" r="16.5" fill="none" stroke="#2b2b2d" stroke-width="2"/><path d="M12.5 10.5c1-.8 2-.6 2.5.3l1.5 2.6c.4.8.2 1.5-.5 2l-1 .8c.8 2 2.3 3.6 4.3 4.6l.9-1c.6-.6 1.3-.7 2-.3l2.6 1.6c.9.5 1 1.6.2 2.5-2 2.2-4.6 1.8-7.4-.4-3-2.4-5.2-5.6-5.8-8.4-.2-1.8.1-3.1.7-4.1z" fill="#2b2b2d"/></svg>
      <svg width="36" height="36" viewBox="0 0 36 36"><circle cx="18" cy="18" r="16.5" fill="none" stroke="#2b2b2d" stroke-width="2"/><rect x="10" y="12" width="16" height="12" fill="#2b2b2d"/><path d="M10.5 12.5 18 18.5l7.5-6M10.5 23.5l5.5-5M25.5 23.5l-5.5-5" fill="none" stroke="#fff" stroke-width="1.2"/></svg>
      <svg width="36" height="36" viewBox="0 0 36 36"><circle cx="18" cy="18" r="16.5" fill="none" stroke="#2b2b2d" stroke-width="2"/><rect x="10.5" y="11" width="15" height="10.5" fill="none" stroke="#2b2b2d" stroke-width="1.8"/><path d="M18 21.5v3.5M14 25.5h8" stroke="#2b2b2d" stroke-width="1.8"/></svg>
      <svg width="36" height="36" viewBox="0 0 36 36"><circle cx="18" cy="18" r="16.5" fill="none" stroke="#2b2b2d" stroke-width="2"/><path d="M18 27c-3.5-4.5-6-8-6-11a6 6 0 0 1 12 0c0 3-2.5 6.5-6 11z" fill="#2b2b2d"/><circle cx="18" cy="16" r="2.2" fill="#fff"/></svg>
    </div>
    <div class="contact-details">
      <p class="contact-phone">03 5900 1234</p>
      <p class="contact-line">stay@harbourretreats.com.au</p>
      <p class="contact-line contact-line--web">harbourretreats.com.au</p>
      <p class="contact-line">PO Box 12, Seaview Victoria 3900</p>
    </div>
    <span class="contact-bar"></span>
  </section>
</main>
</body>
</html>
```